Silver Birch Decorators Banner

Create a banner that displays and reinforces Silver Birch Decorators’ brand identity while promoting our interior painting services. The banner will be displayed at indoor venues through the winter. The design should be clean, professional, and visually recognizable to both new and returning customers. See attached design brief & logo source files.

```html
<!DOCTYPE html>
<html lang="en">
<head>
<meta charset="utf-8">
<title>Silver Birch Decorators – Interior Painting Banner</title>
<link rel="stylesheet" href="https://fonts.googleapis.com/css2?family=Anton&family=Oswald:wght@600&family=Raleway:ital,wght@0,700;0,800;1,800;1,900&family=Montserrat:wght@700;800&family=Roboto+Condensed:wght@400;700&display=swap">
<style>
  :root {
    --brand-green: #76985a;
    --brand-charcoal: #4d4f4d;
    --banner-white: #ffffff;
    --page-bg: #e9ece8;
  }
  * { box-sizing: border-box; margin: 0; padding: 0; }
  html, body {
    width: 1200px; height: 840px; overflow: hidden;
    background: var(--page-bg);
  }
  .banner {
    position: absolute; left: 30px; top: 194px;
    width: 1140px; height: 452px;
    background: var(--banner-white);
    overflow: hidden;
    box-shadow: 0 6px 24px rgba(0,0,0,0.15);
  }
  .banner__bands { position: absolute; inset: 0; }
  .band--green { fill: var(--brand-green); }
  .band--charcoal { fill: var(--brand-charcoal); }

  .brand {
    position: absolute; left: 42px; top: 84px; width: 430px;
    display: flex; align-items: flex-start; gap: 18px;
  }
  .brand__mark {
    flex: none; width: 26px; height: 26px; margin-top: 14px;
    background: var(--brand-green);
  }
  .brand__name {
    font-family: "Montserrat", sans-serif; font-weight: 800;
    color: var(--brand-charcoal);
    font-size: 58px; line-height: 1.02; letter-spacing: 0.5px;
    text-transform: uppercase;
  }

  .cta { position: absolute; left: 38px; top: 330px; width: 460px; }
  .cta__prompt {
    font-family: "Raleway", sans-serif; font-weight: 800;
    font-size: 24px; color: var(--brand-charcoal);
    padding-left: 50px;
  }
  .cta__prompt em { font-style: italic; font-weight: 900; }
  .cta__url {
    font-family: "Roboto Condensed", sans-serif; font-weight: 400;
    font-size: 46px; color: var(--banner-white); line-height: 1.1;
    margin-top: 4px; white-space: nowrap;
  }
  .cta__url strong { font-weight: 700; }

  .offer {
    position: absolute; right: 34px; top: 22px; width: 560px;
    text-align: right;
  }
  .offer__headline {
    font-family: "Anton", sans-serif; color: var(--brand-green);
    font-size: 128px; line-height: 1; letter-spacing: 2px;
  }
  .offer__subhead {
    font-family: "Oswald", sans-serif; font-weight: 600;
    color: var(--brand-charcoal);
    font-size: 52px; line-height: 1; margin-top: 6px; letter-spacing: 0.5px;
  }
  .offer__rule {
    width: 296px; height: 2px; background: var(--brand-charcoal);
    margin: 20px 0 14px auto;
  }
  .services {
    list-style: none; display: flex; flex-wrap: wrap;
    justify-content: flex-end; column-gap: 16px; row-gap: 10px;
  }
  .services__item {
    display: flex; align-items: center; gap: 4px;
    font-family: "Raleway", sans-serif; font-style: italic; font-weight: 900;
    font-size: 32px; color: var(--brand-green); line-height: 1.1;
  }
  .services__tick { width: 28px; height: 28px; flex: none; }
  .services__tick rect, .services__tick path {
    fill: none; stroke: var(--brand-charcoal); stroke-width: 3;
    stroke-linecap: round; stroke-linejoin: round;
  }
  .services__tick path { stroke-width: 4; }
  .services__break { flex-basis: 100%; height: 0; }

  .tagline {
    position: absolute; right: 42px; top: 384px;
    font-family: "Montserrat", sans-serif; font-weight: 700;
    font-size: 21px; color: var(--banner-white); letter-spacing: 0.2px;
  }
</style>
</head>
<body>
  <main class="banner">
    <svg class="banner__bands" viewBox="0 0 1140 452" width="1140" height="452" aria-hidden="true">
      <path class="band--green" d="M0,318 L462,314 Q494,314 510,340 L552,414 Q568,440 600,440 L1140,436 L1140,452 L0,452 Z"/>
      <path class="band--charcoal" d="M540,374 L1140,368 L1140,430 L602,434 Q576,434 563,412 Z"/>
    </svg>

    <div class="brand">
      <span class="brand__mark"></span>
      <p class="brand__name">Silver Birch<br>Decorators</p>
    </div>

    <div class="cta">
      <p class="cta__prompt">Book Your <em>Free</em> Estimate</p>
      <p class="cta__url">www.<strong>silverbirchdeco</strong>.com</p>
    </div>

    <section class="offer">
      <h1 class="offer__headline">INTERIOR</h1>
      <h2 class="offer__subhead">PAINTING SERVICES</h2>
      <div class="offer__rule"></div>
      <ul class="services">
        <li class="services__item"><svg class="services__tick" viewBox="0 0 28 28"><rect x="2" y="5" width="20" height="20" rx="3"/><path d="M7 14 L12 20 L25 3"/></svg>Walls</li>
        <li class="services__item"><svg class="services__tick" viewBox="0 0 28 28"><rect x="2" y="5" width="20" height="20" rx="3"/><path d="M7 14 L12 20 L25 3"/></svg>Ceilings</li>
        <li class="services__item"><svg class="services__tick" viewBox="0 0 28 28"><rect x="2" y="5" width="20" height="20" rx="3"/><path d="M7 14 L12 20 L25 3"/></svg>Trim</li>
        <li class="services__break"></li>
        <li class="services__item"><svg class="services__tick" viewBox="0 0 28 28"><rect x="2" y="5" width="20" height="20" rx="3"/><path d="M7 14 L12 20 L25 3"/></svg>Cabinets</li>
        <li class="services__item"><svg class="services__tick" viewBox="0 0 28 28"><rect x="2" y="5" width="20" height="20" rx="3"/><path d="M7 14 L12 20 L25 3"/></svg>Drywall Repair</li>
      </ul>
    </section>

    <p class="tagline">Trusted Local Professionals Since 2005</p>
  </main>
</body>
</html>
```